Business Card Design - Photographer

I am a landscape photographer and I require a business card design. 

I require two designs:
1)  a double sided business card
 and
b)  a single sided business card 

The single sided design can either be the same as the double sided (with just one side having all the information)....or it can be an entire new design. Its up to you.

My corporate colours are (CMYK):

Blue   69, 32, 0, 0
Grey  72,  64,  47,  31
Green  32,  2,  91,  0
Yellow   0, 19, 92, 0
Orange  0, 39, 75, 0

Colour space in final file should be in CMYK.

The details that need to be included on the card:

- Use the provided Logo
- Name: Lukas Wendrovski
- Email:   sales@vistaplume.com.au
- Website:    vistaplume.com.au
- Twitter:    twitter.com/vistaplume
- Facebook:   facebook.com/vistaplume
- Mobile  0415 309 662

Please use the attached template to design the logo to the specified size, including the marked bleed lines. I have also attached my logo in PNG (transparent background) and ai format for you to use.

The final file should be:
- Photoshop version with layers so I can edit the name/text etc. All non vector files should be high resolution at 1039 x 697 pixels at 300 dpi.

I also require a file as:
- Vector based PDF

Anyway questions please contact me.

Thank you

Industry/Entity Type

Landscape

Logo styles of interest
Pictorial/Combination Logo
Abstract Logo
Wordmark Logo
Lettermark Logo
Requirements
Must have
• The details that need to be included on the card:

- Use the provided Logo
- Name: Lukas Wendrovski
- Email: sales@vistaplume.com.au
- Website: vistaplume.com.au
- Twitter: twitter.com/vistaplume
- Facebook: facebook.com/vistaplume
- Mobile 0415 309 662

```html
<!DOCTYPE html>
<html lang="en">
<head>
<meta charset="utf-8">
<title>Vista Plume – single sided business card</title>
<link href="https://fonts.googleapis.com/css2?family=Source+Sans+3:wght@400;600&display=swap" rel="stylesheet">
<style>
  :root {
    --stage: #2b2522;
    --card-black: #121212;
    --card-green: #a6c22c;
    --card-blue: #1f63ad;
    --name-green: #7fa323;
    --ink-light: #f2f2f2;
    --ink-dark: #1b1b1b;
    --leaf-orange: #f39a2b;
    --leaf-green: #8dbb25;
    --leaf-blue: #2d6fc0;
  }
  * { box-sizing: border-box; margin: 0; padding: 0; }
  html, body {
    width: 1200px; height: 800px; overflow: hidden;
    background: var(--stage);
    font-family: "Source Sans 3", Arial, sans-serif;
  }
  .sheet {
    width: 1200px; height: 800px;
    display: grid;
    grid-template-columns: 560px 560px;
    grid-template-rows: 367px 367px;
    gap: 20px;
    justify-content: center;
    align-content: center;
  }
  .card { position: relative; overflow: hidden; }
  .card--contact { background: var(--card-black); }
  .card--green { background: var(--card-green); }
  .card--blue { background: var(--card-blue); }

  .leaf-field {
    position: absolute; left: 55%; top: 26%; width: 45%; height: 74%;
    background:
      radial-gradient(ellipse at 65% 70%, rgba(243,154,43,0.16), transparent 60%),
      radial-gradient(ellipse at 35% 40%, rgba(45,111,192,0.14), transparent 60%),
      radial-gradient(ellipse at 80% 30%, rgba(141,187,37,0.12), transparent 55%);
  }

  .contact {
    position: absolute; right: 46%; top: 41%;
    text-align: right;
    transform: rotate(-8deg);
    transform-origin: right center;
    line-height: 1.2;
  }
  .contact__name { color: var(--name-green); font-weight: 600; font-size: 23px; }
  .contact__line { color: var(--ink-light); font-size: 17px; }

  .brand {
    position: absolute; left: 0; right: 0; top: 55%;
    display: flex; justify-content: center; align-items: center; gap: 12px;
  }
  .brand__dot { width: 22px; height: 22px; border-radius: 50%; background: var(--ink-dark); }
  .brand__name {
    color: var(--ink-dark); font-weight: 600; font-size: 26px;
    letter-spacing: 1px; text-transform: uppercase;
  }

  .social {
    position: absolute; left: 0; right: 0; top: 83%;
    display: flex; justify-content: center; gap: 24px;
    color: var(--ink-dark); font-size: 14px;
  }
  .social__item { display: flex; align-items: center; gap: 6px; }
  .social__mark { width: 14px; height: 14px; border-radius: 2px; background: var(--ink-dark); }
  .card--green .social__mark { background: var(--leaf-blue); }
  .card--blue .social__mark { background: #e8eef7; }
</style>
</head>
<body>
<main class="sheet">
  <section class="card card--contact">
    <div class="leaf-field" role="img" aria-label="Scattered small falling leaves in orange, green and blue"></div>
    <div class="contact">
      <p class="contact__name">Lukas Wendrovski</p>
      <p class="contact__line">m. 0415 309 662</p>
      <p class="contact__line">sales@vistaplume.com.au</p>
    </div>
  </section>

  <section class="card card--green">
    <div class="brand"><span class="brand__dot"></span><span class="brand__name">Vista Plume</span></div>
    <div class="social">
      <span class="social__item"><span class="social__mark"></span>vistaplume</span>
      <span class="social__item"><span class="social__mark"></span>vistaplume</span>
    </div>
  </section>

  <section class="card card--contact">
    <div class="leaf-field" role="img" aria-label="Scattered small falling leaves in orange, green and blue"></div>
    <div class="contact">
      <p class="contact__name">Lukas Wendrovski</p>
      <p class="contact__line">m. 0415 309 662</p>
      <p class="contact__line">sales@vistaplume.com.au</p>
    </div>
  </section>

  <section class="card card--blue">
    <div class="brand"><span class="brand__dot"></span><span class="brand__name">Vista Plume</span></div>
    <div class="social">
      <span class="social__item"><span class="social__mark"></span>vistaplume</span>
      <span class="social__item"><span class="social__mark"></span>vistaplume</span>
    </div>
  </section>
</main>
</body>
</html>
```